Lantern's Pick CBD Packaging and Branding

We are looking for packaging designs for a new doctor focused CBD brand that is disease specific formulations (i.e. Bone and Joint Formula, Pelvic Formula, Pain Formula, Inflammation Formula, ect.) We would like the first packaging prototype to be our Pain Formulation. Our tagline is, "The Lantern's Pick" & we would also like the phrase, "Life. Balanced." - We are looking for our Logo to be on the box as well. We currently need a logo as well. We would like the letters "QX" to be more prominent than "vita" Our first product will be SoftGels and the active ingredient list can be made up at the moment. Our brand and packaging needs to convey authority, trust and scientific knowledge (since all of our formulations are created by researched and renowned doctors and scientists), but we also don't want to be too clinical feeling, so adding a modern touch. Attached are some sample designs for reference (none are the final iteration) as well as some vectorized art.

Target Market(s)

40-60 year old patients

Industry/Entity Type

Medical And Science

Logo Text

QX Vita

Requirements
Must have
• Clean, professional and trusting medical designs with a modern touch. New logo incorporated into the design.
Should not have
• Not too clinical feeling - Not pharmaceutical

```html
<!DOCTYPE html>
<html lang="en">
<head>
<meta charset="utf-8">
<title>QX Vita Comfort – Carton Panels</title>
<link rel="stylesheet" href="https://fonts.googleapis.com/css2?family=Montserrat:wght@400;500;600;700&display=swap">
<style>
  :root {
    --backdrop: #5bc2d9;
    --carton: #ffffff;
    --carton-shade: #f1f2f3;
    --teal: #4a9ca3;
    --teal-figure: #3f979f;
    --ink-grey: #6b6d70;
    --ink-dark: #5a5c5f;
  }
  * { box-sizing: border-box; margin: 0; padding: 0; }
  html, body { width: 1200px; height: 1200px; overflow: hidden; }
  body {
    background: var(--backdrop);
    font-family: "Montserrat", sans-serif;
    position: relative;
  }
  .carton-layout {
    position: absolute;
    left: 70px; top: 220px;
    width: 1060px; height: 760px;
    display: flex;
    box-shadow: 0 18px 40px rgba(0,0,0,.12);
  }
  .panel {
    position: relative;
    height: 760px;
    background: var(--carton);
    overflow: hidden;
  }
  .panel--side { width: 150px; background: var(--carton-shade); }
  .panel--main { width: 380px; }
  .panel + .panel { border-left: 1px solid #e2e4e6; }

  .band { position: absolute; left: 0; bottom: 0; width: 100%; height: 110px; }
  .band path { fill: var(--teal); }

  /* brand wordmark */
  .wordmark { position: absolute; text-align: center; color: var(--ink-grey); }
  .wordmark__name { font-weight: 600; line-height: 1; letter-spacing: -1px; white-space: nowrap; }
  .wordmark__tag { font-weight: 500; text-transform: uppercase; letter-spacing: 2px; margin-top: 8px; white-space: nowrap; }

  /* front */
  .front .wordmark { left: 172px; top: 92px; width: 190px; }
  .front .wordmark__name { font-size: 44px; }
  .front .wordmark__tag { font-size: 9.5px; }
  .figure-art {
    position: absolute; left: 24px; top: 100px;
    width: 128px; height: 560px;
    border-radius: 56px 56px 28px 28px;
    background: linear-gradient(180deg, #3f979f 0%, #4aa3aa 60%, #3f979f 100%);
  }
  .product-name {
    position: absolute; left: 176px; top: 446px;
    font-size: 32px; font-weight: 700; color: var(--teal); letter-spacing: 1px;
    white-space: nowrap;
  }
  .product-rule {
    position: absolute; left: 176px; right: 0; top: 490px;
    height: 3px; background: var(--teal);
  }
  .product-detail {
    position: absolute; right: 40px; top: 504px;
    text-align: right; font-size: 14px; font-weight: 600;
    color: var(--ink-dark); line-height: 1.6; text-transform: uppercase;
  }
  .dose {
    position: absolute; right: 40px; bottom: 22px;
    text-align: right; color: #fff; line-height: 1;
  }
  .dose__amount { font-size: 24px; font-weight: 600; }
  .dose__count { font-size: 14px; font-weight: 700; margin-top: 4px; }

  /* back */
  .tagline {
    position: absolute; left: 40px;
    font-weight: 700; color: var(--ink-grey);
    text-transform: uppercase; letter-spacing: 4px; line-height: 1.15;
  }
  .back .tagline--top { top: 110px; font-size: 20px; }
  .back .tagline--bottom { bottom: 150px; font-size: 20px; letter-spacing: 6px; }
  .formula-label {
    position: absolute; left: 24px; bottom: 28px;
    color: #fff; font-size: 14px; font-weight: 600; letter-spacing: 6px;
  }

  /* left side */
  .side-tagline {
    position: absolute; left: 16px; top: 100px;
    font-size: 13px; font-weight: 600; color: var(--ink-dark);
    text-transform: uppercase; line-height: 1.4;
  }
  .ingredients { position: absolute; left: 0; right: 16px; top: 400px; }
  .ingredients__title {
    font-size: 10px; font-weight: 600; color: var(--teal);
    text-transform: uppercase; padding: 6px 0 4px 16px;
    border-top: 1.5px solid var(--teal); border-bottom: 1.5px solid var(--teal);
  }
  .ingredients__list {
    list-style: none; padding: 8px 0 0 16px;
    font-size: 10px; color: var(--ink-dark); text-transform: uppercase; line-height: 2;
  }
  .side-band-label {
    position: absolute; left: 14px; bottom: 18px;
    color: #fff; font-size: 11px; font-weight: 600; letter-spacing: 2px;
  }

  /* right side */
  .side-wordmark { left: 0; width: 100%; top: 80px; }
  .side-wordmark .wordmark__name { font-size: 32px; }
  .side-wordmark .wordmark__tag { font-size: 7px; letter-spacing: 1.5px; }
  .copy {
    position: absolute; left: 14px; right: 14px; top: 300px;
    font-size: 8.5px; line-height: 1.7; color: var(--ink-dark);
  }
  .copy p + p { margin-top: 40px; }
  .side-dose {
    position: absolute; right: 14px; bottom: 14px;
    color: #fff; text-align: right; line-height: 1.1;
  }
  .side-dose b { display: block; font-size: 14px; font-weight: 600; }
  .side-dose span { font-size: 9px; font-weight: 700; }
</style>
</head>
<body>
<main class="carton-layout">

  <section class="panel panel--side side-left">
    <p class="side-tagline">Life.<br>Balanced.</p>
    <div class="ingredients">
      <h3 class="ingredients__title">Active Ingredient</h3>
      <ul class="ingredients__list">
        <li>Cannabidiol</li><li>L-Theanine</li><li>Magnesium</li><li>Citrate</li>
        <li>Ginco</li><li>Aswwagandha</li><li>Thiamin</li><li>Aisfolavin</li>
        <li>GABA</li><li>Holy Basil</li>
      </ul>
    </div>
    <svg class="band" viewBox="0 0 150 110" preserveAspectRatio="none" aria-hidden="true">
      <path d="M0 50 H150 V110 H0 Z"/>
    </svg>
    <span class="side-band-label">FORMULA</span>
  </section>

  <section class="panel panel--main front">
    <svg class="band" viewBox="0 0 380 110" preserveAspectRatio="none" aria-hidden="true">
      <path d="M0 75 H150 Q168 75 174 55 L180 35 Q186 18 205 18 H380 V110 H0 Z"/>
    </svg>
    <div class="figure-art" role="img" aria-label="Teal anatomical muscle figure illustration of a standing human body"></div>
    <div class="wordmark">
      <div class="wordmark__name">QX vita</div>
      <div class="wordmark__tag">The Lantern's Pick</div>
    </div>
    <h1 class="product-name">COMFORT</h1>
    <div class="product-rule"></div>
    <p class="product-detail">Pain Formulation<br>Softgels</p>
    <div class="dose">
      <div class="dose__amount">60mg CBD</div>
      <div class="dose__count">30 COUNT</div>
    </div>
  </section>

  <section class="panel panel--main back">
    <p class="tagline tagline--top">Life.<br>Balanced.</p>
    <p class="tagline tagline--bottom">The<br>Lantern's<br>Pick</p>
    <svg class="band" viewBox="0 0 380 110" preserveAspectRatio="none" aria-hidden="true">
      <path d="M0 18 H190 Q208 18 214 36 L220 55 Q226 75 246 75 H380 V110 H0 Z"/>
    </svg>
    <span class="formula-label">FORMULA</span>
  </section>

  <section class="panel panel--side side-right">
    <div class="wordmark side-wordmark">
      <div class="wordmark__name">QX vita</div>
      <div class="wordmark__tag">The Lantern's Pick</div>
    </div>
    <div class="copy">
      <p>Each softgel delivers a measured dose of broad spectrum hemp extract blended with calming botanicals and minerals. Take one softgel daily with food or as directed by your physician. Store in a cool, dry place away from direct light.</p>
      <p>Formulated by physicians and researchers to support everyday comfort. Not intended to diagnose, treat, cure or prevent any disease. Consult your doctor before use if pregnant, nursing or taking medication. Keep out of reach of children.</p>
    </div>
    <svg class="band" viewBox="0 0 150 110" preserveAspectRatio="none" aria-hidden="true">
      <path d="M0 50 H150 V110 H0 Z"/>
    </svg>
    <div class="side-dose"><b>60mg CBD</b><span>30 COUNT</span></div>
  </section>

</main>
</body>
</html>
```